Two flyers with cover pages for business services company

We need to create two double sided A4 flyers for our company. We are a company that provides professional services for businesses in Dubai, UAE.
Please note that there are two different flyers. The design must be identical. Each has a cover page. The cover page will be duplicated for both flyers.
Please note that we have added images of the Dubai skyline, clip art as place-hold/temporary images. These can be changed to be more fitting to your design. We prefer to have free images where possible but are open to purchasing Pixelorra images if required.
We have recommended a colour palet below. You are welcome to change some colours to be more fitting to the design. However, we must have black, white and blue and per the logo.
Target Market(s)
Businesses, entrepreneurs, professionals
Industry/Entity Type
Business Service
Requirements
Must have
- The cover page should be less crowded and more visual. So mostly images with our logo and tagline.

```html
<!DOCTYPE html>
<html lang="en">
<head>
<meta charset="utf-8">
<title>Novira Flyers</title>
<link rel="stylesheet" href="https://fonts.googleapis.com/css2?family=Asap+Condensed:wght@400;600;700&family=Barlow+Condensed:ital,wght@0,300;0,400;0,500;0,600;1,500&family=Open+Sans:wght@400&display=swap">
<style>
:root{
  --bg:#e3e3e3;
  --paper:#ffffff;
  --orange:#e0821f;
  --orange-bright:#f39325;
  --navy:#1d3545;
  --blue:#1f5aa6;
  --blue-circle:#2e72b6;
  --sky-top:#8bbbe8;
  --sky-bottom:#d5e6f3;
  --ink:#222;
  --grey:#4a4a4a;
}
*{margin:0;padding:0;box-sizing:border-box}
html,body{width:1200px;height:1200px;overflow:hidden;background:var(--bg)}
.canvas{position:relative;width:1200px;height:1200px}
.flyer{position:absolute;top:187px;width:556px;height:787px;background:var(--paper);box-shadow:0 2px 8px rgba(0,0,0,.18);overflow:hidden}
.cover{left:28px}
.inside{left:607px}

/* cover */
.cover-band{position:absolute;left:0;top:0;width:100%;height:191px;background:var(--orange)}
.cover-headline{position:absolute;left:0;top:18px;width:100%;text-align:center;font-family:"Asap Condensed",sans-serif;font-weight:600;font-size:46px;line-height:47px;color:var(--navy);letter-spacing:-.3px}
.cover-headline b{font-weight:700}
.cover-sky{position:absolute;left:0;top:191px;width:100%;height:596px;background:linear-gradient(180deg,var(--sky-top) 0%,#a7cbec 60%,var(--sky-bottom) 100%)}
.cover-photo{position:absolute;left:90px;top:165px;width:300px;height:622px;background:linear-gradient(180deg,#f2f2f2,#e3e7ea);border-radius:120px 120px 0 0;opacity:.9}
.brand{position:absolute;left:316px;top:672px;display:flex;align-items:center;gap:10px}
.brand-dot{width:42px;height:42px;border-radius:50%;background:#2a9be0}
.brand-name{font-family:"Asap Condensed",sans-serif;font-weight:400;font-size:44px;color:var(--navy);letter-spacing:1px}
.brand-url{position:absolute;left:356px;top:730px;font-family:"Open Sans",sans-serif;font-size:19px;color:var(--navy);letter-spacing:.5px}

/* inside */
.inside-title{position:absolute;left:19px;top:20px;font-family:"Barlow Condensed",sans-serif;font-weight:400;font-size:31px;line-height:34px;color:var(--blue)}
.team-photo{position:absolute;left:0;top:99px;width:100%;height:258px;background:linear-gradient(135deg,#eef0f2 0%,#d7dadd 55%,#bfc3c7 100%)}
.badge{position:absolute;left:31px;width:140px;height:140px;border-radius:50%;background:var(--blue-circle);border:5px solid var(--orange-bright);display:flex;flex-direction:column;justify-content:center;align-items:center;text-align:center;color:#fff;font-family:"Barlow Condensed",sans-serif;font-weight:300;font-size:18px;line-height:16px;box-shadow:0 2px 4px rgba(0,0,0,.2)}
.badge b{font-weight:600}
.badge-installments{top:341px}
.badge-guarantee{top:497px}
.section-head{position:absolute;left:183px;font-family:"Barlow Condensed",sans-serif;font-weight:400;font-size:19px;color:var(--blue)}
.head-network{top:372px}
.head-offer{top:448px}
.network-text{position:absolute;left:183px;top:399px;font-family:"Barlow Condensed",sans-serif;font-weight:400;font-size:15px;line-height:20px;color:var(--ink)}
.network-text b{font-weight:500}
.offer-list{position:absolute;left:183px;top:476px;list-style:none;font-family:"Barlow Condensed",sans-serif;font-weight:300;font-size:14px;line-height:18.5px;color:var(--ink)}
.offer-list li::before{content:"- "}
.offer-list b{font-weight:600}
.cta-label{position:absolute;left:21px;top:669px;font-family:"Barlow Condensed",sans-serif;font-weight:300;font-size:15px;color:var(--grey)}
.cta-label b{font-weight:500;color:var(--ink)}
.cta-phone{position:absolute;left:20px;top:686px;font-family:"Barlow Condensed",sans-serif;font-weight:400;font-size:37px;color:var(--orange-bright)}
.contact{position:absolute;top:733px;display:flex;align-items:center;gap:6px;font-family:"Barlow Condensed",sans-serif;font-weight:300;font-size:13px;line-height:13px;color:var(--ink)}
.contact-address{left:22px}
.contact-web{left:191px}
.person-tag{position:absolute;left:425px;top:683px;width:110px;height:61px;background:var(--orange-bright);padding:12px 0 0 38px;color:#fff;font-family:"Barlow Condensed",sans-serif}
.person-name{font-weight:500;font-size:17px;line-height:18px}
.person-role{font-style:italic;font-weight:500;font-size:12px}
.person-photo{position:absolute;left:321px;top:657px;width:112px;height:112px;border-radius:50%;border:3px solid var(--orange-bright);background:linear-gradient(180deg,#d8dde2,#8c96a3)}
</style>
</head>
<body>
<div class="canvas">

  <section class="flyer cover">
    <div class="cover-sky" role="img" aria-label="Faded Dubai skyline in pale blue"></div>
    <div class="cover-band"></div>
    <h1 class="cover-headline">Are you getting <b>REAL</b><br>value from<br>your current sponsor?</h1>
    <div class="cover-photo" role="img" aria-label="Smiling businessman in white kandura and ghutra holding a briefcase"></div>
    <div class="brand"><span class="brand-dot"></span><span class="brand-name">Novira</span></div>
    <div class="brand-url">www.novira.ae</div>
  </section>

  <section class="flyer inside">
    <h2 class="inside-title">DO YOU NEED HELP TO INCREASE<br>YOUR SALES?</h2>
    <div class="team-photo" role="img" aria-label="Three businessmen reviewing documents together at a desk"></div>

    <div class="badge badge-installments">AS LOW AS<br><b>1,500 AED</b> EASY<br>MONTHLY<br>INSTALLMENTS</div>
    <div class="badge badge-guarantee"><b>SATISFACTION<br>GUARANTEED</b><br>100%<br>OR YOUR<br>MONEY BACK</div>

    <h3 class="section-head head-network">Grow Your Business Through Our Extensive Network</h3>
    <p class="network-text">Use our <b>3,000+ Business Connections,</b><br><b>570+Decision Makers,</b> MDs, CEO's, Heads of Purchasing</p>

    <h3 class="section-head head-offer">The Best Offer in the Market</h3>
    <ul class="offer-list">
      <li><b>50% off</b> your current sponsorship fees</li>
      <li><b>Free sponsorship</b> for 12 months</li>
      <li>Low monthly installments (starting at&nbsp; AED 1,500)</li>
      <li>We can be active or silent sponsors</li>
      <li>Unique legal structure which allows you to exit any time</li>
      <li>Help you increase your sales</li>
      <li>VIP introductions and connections</li>
      <li>Legal and mediation support</li>
      <li>We have been in this market since 2004</li>
    </ul>

    <p class="cta-label">CALL US NOW FOR A <b>FREE CONSULTATION</b> ON</p>
    <p class="cta-phone">04 555 0199</p>
    <div class="contact contact-address">
      <svg width="16" height="24" viewBox="0 0 16 24"><path d="M8 1a7 7 0 0 0-7 7c0 5 7 15 7 15s7-10 7-15a7 7 0 0 0-7-7z" fill="none" stroke="#222" stroke-width="2"/><circle cx="8" cy="8" r="2.5" fill="#222"/></svg>
      <span>Al Noor Business Tower,<br>24th Floor Dubai, UAE</span>
    </div>
    <div class="contact contact-web">
      <svg width="22" height="22" viewBox="0 0 22 22" fill="none" stroke="#222" stroke-width="1.4"><circle cx="11" cy="11" r="10"/><ellipse cx="11" cy="11" rx="4.5" ry="10"/><path d="M1 11h20M3 6h16M3 16h16"/></svg>
      <span>www.novira.ae</span>
    </div>

    <div class="person-tag"><div class="person-name">Daniel Hart,</div><div class="person-role">Managing Director</div></div>
    <div class="person-photo" role="img" aria-label="Portrait of the managing director in a suit"></div>
  </section>

</div>
</body>
</html>
```